Wentworth Real Estate Partners Looking For FUNNY, SEXY & KICK ASS Billboards!

We are launching our billboard campaign Jan 2021 and will need 8 billboards. We have some hilarious ideas but need a professional to help us! We are a male and female based real estate partnership selling commercial and residential properties in New Brunswick Canada. We have a lot of ideas but need direction.

Target Market(s)

Sellers and Buyers of Real Estate

Industry/Entity Type

Real Estate Agent

Font styles to use
Serif

Colors

Designer to choose only greyscale colors for use in the design.

Requirements
Must have
• Funny, sassy and eye-catching. We like to have fun and want out billboards to make people smile.
Nice to have
• Movies references having to do with real estate (we have ideas) WE would like the project to be cohesive over the 8 billboards.
Should not have
• Too much colour or too generic. We have our brand colours we would like to stick with. Black, white and red accent.

```html
<!DOCTYPE html>
<html lang="en">
<head>
<meta charset="utf-8">
<title>We Want Your Listing – Billboard</title>
<link rel="stylesheet" href="https://fonts.googleapis.com/css2?family=Montserrat:wght@400;500;600;800;900&display=swap">
<style>
  :root {
    --page: #f1f1f1;
    --ink: #111111;
    --red: #e0232f;
    --board-light: #ffffff;
    --board-mid: #e4e6e9;
    --board-dark: #c3c7cd;
    --skin-light: #f3d2bc;
    --skin-dark: #d9a88a;
  }
  * { margin: 0; padding: 0; box-sizing: border-box; }
  html, body {
    width: 889px; height: 1200px; overflow: hidden;
    background: var(--page);
    font-family: "Montserrat", sans-serif;
    color: var(--ink);
  }
  .billboard {
    position: absolute; left: 24px; top: 390px;
    width: 840px; height: 420px; overflow: hidden;
    background: radial-gradient(ellipse at 70% 35%, var(--board-light) 0%, var(--board-mid) 55%, var(--board-dark) 100%);
    box-shadow: 0 4px 10px rgba(0,0,0,0.18);
  }
  .brand {
    position: absolute; left: 41px; top: 28px;
    display: flex; align-items: center; gap: 8px;
  }
  .brand-mark { width: 26px; height: 26px; background: var(--red); }
  .brand-name {
    font-weight: 800; font-size: 17px; letter-spacing: 0.5px; line-height: 1.05;
    color: var(--ink); text-transform: uppercase;
  }
  .headline-light {
    position: absolute; left: 38px; top: 92px;
    font-weight: 400; font-size: 63px; line-height: 1; letter-spacing: 1px;
  }
  .headline-bold {
    position: absolute; left: 37px; top: 150px;
    font-weight: 900; font-size: 62px; line-height: 1; color: var(--red); letter-spacing: -0.5px;
  }
  .divider {
    position: absolute; left: 39px; top: 220px; width: 455px; height: 1.5px; background: var(--ink);
  }
  .divider-accent {
    position: absolute; left: 59px; top: 217px; width: 64px; height: 7px;
    border-radius: 4px; background: var(--red);
  }
  .tagline {
    position: absolute; left: 39px; top: 243px;
    font-weight: 800; font-size: 24px; line-height: 26px; letter-spacing: 0.8px; text-transform: uppercase;
  }
  .subline {
    position: absolute; left: 39px; top: 300px;
    font-weight: 400; font-size: 16px; letter-spacing: 0.3px;
  }
  .call {
    position: absolute; left: 38px; top: 332px;
    font-weight: 800; font-size: 35px; line-height: 1; letter-spacing: 0.5px; white-space: nowrap;
  }
  .call-label { color: var(--red); }
  .contact {
    position: absolute; left: 39px; top: 378px;
    display: flex; gap: 14px; font-weight: 500; font-size: 9.5px; line-height: 12px; letter-spacing: 0.3px;
  }
  .contact-item { display: flex; align-items: flex-start; gap: 6px; }
  .contact-item svg { flex: none; margin-top: 1px; }
  .photo-hands {
    position: absolute; right: 0; top: 0; width: 300px; height: 420px;
    background:
      radial-gradient(ellipse 60% 18% at 65% 18%, var(--skin-light) 0%, rgba(243,210,188,0) 70%),
      radial-gradient(ellipse 55% 12% at 55% 82%, var(--skin-light) 0%, rgba(243,210,188,0) 70%),
      radial-gradient(ellipse 30% 16% at 38% 68%, #e8cfae 0%, rgba(232,207,174,0) 75%),
      linear-gradient(160deg, rgba(217,168,138,0) 40%, rgba(217,168,138,0.35) 100%);
  }
</style>
</head>
<body>
  <section class="billboard">
    <div class="brand">
      <span class="brand-mark"></span>
      <span class="brand-name">Harbourline Realty</span>
    </div>

    <h1 class="headline-light">WE WANT</h1>
    <h2 class="headline-bold">YOUR LISTING</h2>

    <div class="divider"></div>
    <div class="divider-accent"></div>

    <p class="tagline">There's a new sheriff<br>in town</p>
    <p class="subline">This could be us, but you're renting....</p>

    <p class="call"><span class="call-label">CALL NOW</span> (506) 555-0142</p>

    <div class="contact">
      <div class="contact-item">
        <svg width="8" height="10" viewBox="0 0 8 10" aria-hidden="true">
          <path d="M4 0a4 4 0 0 1 4 4c0 3-4 6-4 6S0 7 0 4a4 4 0 0 1 4-4z" fill="#e0232f"/>
          <circle cx="4" cy="4" r="1.5" fill="#fff"/>
        </svg>
        <span>Harbourline Atlantic 48 Maple Row Saint<br>John, NB, E2K 1A1</span>
      </div>
      <div class="contact-item">
        <svg width="10" height="10" viewBox="0 0 10 10" aria-hidden="true">
          <circle cx="5" cy="5" r="4.4" fill="none" stroke="#e0232f" stroke-width="1.1"/>
          <ellipse cx="5" cy="5" rx="2" ry="4.4" fill="none" stroke="#e0232f" stroke-width="0.9"/>
          <line x1="0.6" y1="5" x2="9.4" y2="5" stroke="#e0232f" stroke-width="0.9"/>
        </svg>
        <span>www.wentworthrealestate.ca</span>
      </div>
      <div class="contact-item">
        <svg width="11" height="8" viewBox="0 0 11 8" aria-hidden="true">
          <rect width="11" height="8" fill="#e0232f"/>
          <path d="M0.5 0.5 5.5 4.5 10.5 0.5" fill="none" stroke="#fff" stroke-width="1"/>
        </svg>
        <span>jmorrow@harbourline.ca</span>
      </div>
    </div>

    <div class="photo-hands" role="img" aria-label="Photo of one hand dangling a house key above another open hand holding a small wooden house model"></div>
  </section>
</body>
</html>
```